clearwater mental health web page

this is to be a single page with no links - will function just like an add.
will have 2 biographies
contact info.
Updates

Dear Designers - most of these are too complex.

 Just want one page with contact details (yet to be sorted). No email contact as we can't monitor all emails and if person emails saying suicidal I am potentially accountable if they are successful. Hence- this is just like a listing in a phone book. 
2 photos - one of me the other my husband - with a little blurb next to our names.
No info on fees or appointments etc
I am legally not allowed use language like - "what sets us apart" - it suggests we are better than other clinicians and that is illegal. 
NO EMOTIVE PHOTOS PLEASE! 

Target Market(s)

clients wanting check background and contact information.

Industry/Entity Type

Mental Health

Requirements
Must have
• NEW LOGO
space for photographs
Old web page to complicated
http://lmtq.example.au/index.shtml
Should not have
• anything that flashes.

```html
<!DOCTYPE html>
<html lang="en">
<head>
<meta charset="utf-8">
<title>Clearwater Mental Health</title>
<link href="https://fonts.googleapis.com/css2?family=Questrial&family=Signika:wght@400;600;700&display=swap" rel="stylesheet">
<style>
:root{
  --navy:#0b3a6e;
  --navy-deep:#072c57;
  --grey-text:#6b6b6b;
  --dark-text:#4a4a4a;
  --header-bg:#f7f7f7;
  --card-bg:#f3f3f4;
  --page-bg:#ffffff;
  --footer-top:#2d6aa8;
  --footer-bottom:#0f4a86;
  --icon-grey:#b8b8b8;
}
*{margin:0;padding:0;box-sizing:border-box}
html,body{width:1200px;height:1115px;overflow:hidden;background:var(--page-bg)}
body{font-family:"Questrial",sans-serif;color:var(--navy);position:relative}
.abs{position:absolute}

/* header */
.site-header{left:0;top:0;width:1200px;height:133px;background:var(--header-bg)}
.brand{left:192px;top:29px;display:flex;align-items:center;gap:16px}
.brand-square{width:72px;height:72px;background:var(--navy)}
.brand-name{color:var(--navy);font-size:31px;line-height:34px;letter-spacing:1px}
.brand-name small{display:block;font-size:17px;line-height:22px;letter-spacing:1.5px;color:var(--dark-text)}
.company{right:198px;top:31px;text-align:right;font-family:"Signika",sans-serif;font-weight:400;color:var(--navy);font-size:23px;line-height:25px}
.contact-line{right:198px;top:92px;display:flex;align-items:center;gap:12px;font-size:19px;color:var(--dark-text)}
.contact-line svg{width:25px;height:25px}

/* hero */
.hero{left:0;top:133px;width:1200px;height:520px;background:linear-gradient(90deg,#e9ecef 0%,#f4f1ee 20%,#f7f8fa 45%,#eef3f8 70%,#dbe6f2 90%,#cfdced 100%)}
.hero-shadow{left:0;top:651px;width:1200px;height:4px;background:linear-gradient(#444,#999)}
.hero-title{right:194px;top:179px;text-align:right;font-size:34px;font-weight:400;color:var(--grey-text);line-height:44px}
.hero-name{right:194px;top:223px;text-align:right;font-size:35px;font-weight:400;color:var(--navy);line-height:46px;letter-spacing:.5px}
.hero-sub{right:194px;top:266px;text-align:right;font-size:22px;color:var(--grey-text);line-height:30px}
.services-title{left:521px;top:398px;font-size:23px;font-weight:400;color:var(--navy)}
.service{font-size:14px;color:var(--navy);line-height:23px;display:flex;gap:12px;width:240px}
.service svg{flex:none;width:18px;height:16px;margin-top:4px}

/* bios */
.bio-card{top:714px;height:302px;background:var(--card-bg)}
.bio-photo-frame{top:709px;width:146px;height:302px;background:#fff;border:1px solid #d6d6d6}
.bio-photo{position:absolute;left:0;top:0;width:144px;height:236px}
.bio-caption{position:absolute;left:8px;top:239px;font-size:14px;color:var(--dark-text);line-height:15px}
.bio-caption strong{display:block;font-family:"Signika",sans-serif;font-weight:700;color:var(--navy);font-size:18px;line-height:22px}
.bio-name{top:721px;font-family:"Signika",sans-serif;font-weight:700;font-size:23px;color:var(--navy-deep);letter-spacing:.5px;white-space:nowrap}
.bio-text{top:754px;width:230px;font-size:16.5px;line-height:18.6px;color:var(--navy);white-space:nowrap}
.bio-text span{color:var(--dark-text)}
.specialty{font-size:19px;color:var(--dark-text);display:flex;align-items:center;gap:14px;line-height:25px}
.specialty svg{width:18px;height:16px}

/* footer */
.site-footer{left:0;top:1061px;width:1200px;height:54px;background:linear-gradient(var(--footer-top),var(--footer-bottom));color:#fff}
.footer-item{top:19px;font-size:11px;display:flex;align-items:center;gap:10px}
.footer-item svg{width:16px;height:16px}
.follow{left:838px;top:13px;font-size:17px;display:flex;align-items:center;gap:12px}
.social-dot{width:27px;height:27px;border-radius:50%;background:var(--icon-grey)}
</style>
</head>
<body>

<svg width="0" height="0" class="abs" aria-hidden="true">
  <defs>
    <symbol id="chevrons" viewBox="0 0 18 16">
      <path d="M1 1l7 7-7 7M9 1l7 7-7 7" fill="none" stroke="#0b3a6e" stroke-width="3"/>
    </symbol>
  </defs>
</svg>

<header class="site-header abs">
  <div class="brand abs">
    <div class="brand-square"></div>
    <div class="brand-name">CLEARWATER<small>MENTAL HEALTH</small></div>
  </div>
  <div class="company abs">Clearwater Mental Health Services Pty Ltd<br>As Trustee P &amp; H Marsh Faimly Trust</div>
  <div class="contact-line abs">
    <svg viewBox="0 0 26 26"><circle cx="13" cy="13" r="13" fill="#c4c4c4"/><path d="M8 7c1-1 2-1 3 0l1 3-2 1c1 2 2 3 4 4l1-2 3 1c1 1 1 2 0 3-3 2-11-6-10-10z" fill="#fff"/></svg>
    <span>9000 1234&nbsp; / &nbsp;040 0123456</span>
  </div>
</header>

<section class="hero abs" role="img" aria-label="Photograph of a smiling clinician in a white coat with a stethoscope, with softly blurred medical staff in the background"></section>
<div class="hero-shadow abs"></div>
<h1 class="hero-title abs">Clinical Psychology &amp; Counselling</h1>
<h2 class="hero-name abs">CLEARWATER MENTAL HEALTH</h2>
<p class="hero-sub abs">counselling, medicolegal and rehabilitation fields</p>

<h3 class="services-title abs">Our Services</h3>
<div class="service abs" style="left:515px;top:449px"><svg><use href="#chevrons"/></svg>Adult Psychology Therapy</div>
<div class="service abs" style="left:515px;top:482px"><svg><use href="#chevrons"/></svg>Psychological Assessment</div>
<div class="service abs" style="left:515px;top:515px"><svg><use href="#chevrons"/></svg>Child Psychological Therapy</div>
<div class="service abs" style="left:515px;top:548px;width:230px"><svg><use href="#chevrons"/></svg>Adolescent Psychological Therapy</div>
<div class="service abs" style="left:785px;top:451px"><svg><use href="#chevrons"/></svg>Relationship Therapy</div>
<div class="service abs" style="left:785px;top:484px"><svg><use href="#chevrons"/></svg>Family Therapy</div>
<div class="service abs" style="left:785px;top:517px"><svg><use href="#chevrons"/></svg>Supervision</div>
<div class="service abs" style="left:785px;top:549px"><svg><use href="#chevrons"/></svg>Counselling</div>

<article>
  <div class="bio-card abs" style="left:191px;width:412px"></div>
  <div class="bio-photo-frame abs" style="left:197px">
    <div class="bio-photo" role="img" aria-label="Portrait photograph of Helena Marsh at her desk" style="background:linear-gradient(160deg,#8a6a52,#d8d4cf 55%,#4a5a6e)"></div>
    <div class="bio-caption"><strong>HELENA MARSH</strong>Member Of The<br>Coastal</div>
  </div>
  <div class="bio-name abs" style="left:364px">HELENA MARSH</div>
  <div class="bio-text abs" style="left:364px">M.Psych <span>(Clinical),</span> M.<br>Genetic Couns., B.A.<br><span>(Psych)</span><br>Reg. no: <span>PSY0000123456</span><br>Provider no: <span>10203</span><br>Member Of The<br>Coastal Psychological<br>Society<br>SPECIALISING In The<br>Treatment Of</div>
  <div class="specialty abs" style="left:365px;top:948px"><svg><use href="#chevrons"/></svg>DEPRESSION</div>
  <div class="specialty abs" style="left:365px;top:973px"><svg><use href="#chevrons"/></svg>ANXIETY</div>
</article>

<article>
  <div class="bio-card abs" style="left:630px;width:397px"></div>
  <div class="bio-photo-frame abs" style="left:630px">
    <div class="bio-photo" role="img" aria-label="Portrait photograph of Dr Ruth Alder in a white coat" style="background:linear-gradient(180deg,#f4f4f4,#e8e2dc 45%,#eef1f4)"></div>
    <div class="bio-caption"><strong>Dr Ruth Alder</strong>Member Of The<br>Coastal</div>
  </div>
  <div class="bio-name abs" style="left:798px">Dr Ruth Alder</div>
  <div class="bio-text abs" style="left:798px">M.Psych <span>(Clinical),</span> M.<br>Genetic Couns., B.A.<br><span>(Psych)</span><br>Reg. no: <span>PSY0000123456</span><br>Provider no: <span>10203</span><br>Member Of The<br>Coastal Psychological<br>Society<br>SPECIALISING In The<br>Treatment Of</div>
  <div class="specialty abs" style="left:799px;top:949px"><svg><use href="#chevrons"/></svg>DEPRESSION</div>
  <div class="specialty abs" style="left:799px;top:974px"><svg><use href="#chevrons"/></svg>ANXIETY</div>
</article>

<footer class="site-footer abs">
  <div class="footer-item abs" style="left:202px">
    <svg viewBox="0 0 16 16"><path d="M3 2c1-1 2-1 3 0l1 3-2 1c1 2 2 3 4 4l1-2 3 1c1 1 1 2 0 3-3 3-13-7-10-10z" fill="#fff"/></svg>
    <span>9000 1234&nbsp; / &nbsp;040 0123456</span>
  </div>
  <div class="footer-item abs" style="left:557px">copyright © 2014 Allrights reserved</div>
  <div class="follow abs"><span>Follow us on</span><span class="social-dot"></span><span class="social-dot"></span></div>
</footer>

</body>
</html>
```